Coastal Body Remedies business is seeking a Business Card Design

We are a new natural therapy business that needs a Business Card Design with an appointment card on the back.

We offer Myotherapy (muscle therapy) services and have a strong focus and commitment to helping people relieve pain and restore movement to their bodies.

I am attaching my business logo for you information.

Business card must contain my logo and have space for name, title, qualifications, phone number, email, web address

Appointment Card on the back of the card must contain space to write next appointment date, time and name of therapist and cancellation policy.

Cancellation Policy
Minimum of 24hrs notice is required prior to appointment time or full treatment fees with apply.

```html
<!DOCTYPE html>
<html lang="en">
<head>
<meta charset="utf-8">
<title>Coastal Body Remedies – Business &amp; Appointment Card</title>
<link rel="stylesheet" href="https://fonts.googleapis.com/css2?family=Lato:wght@400;700;900&display=swap">
<style>
  :root {
    --backdrop: #2b2b2d;
    --card: #ffffff;
    --brand-red: #c8102e;
    --ink: #1c1c1c;
    --muted: #555555;
    --dots: #8a8a8a;
  }
  * { box-sizing: border-box; margin: 0; padding: 0; }
  html, body { width: 1200px; height: 900px; overflow: hidden; }
  body {
    background: var(--backdrop);
    font-family: "Lato", Arial, sans-serif;
    color: var(--ink);
    position: relative;
  }
  .card {
    position: absolute;
    width: 500px;
    height: 290px;
    background: var(--card);
    border-radius: 18px;
    box-shadow: 0 18px 40px rgba(0,0,0,.55);
  }
  .card--appointment { left: 90px; top: 120px; padding: 26px 30px; }
  .card--business { left: 610px; top: 490px; }

  /* Appointment side */
  .label {
    display: inline-block;
    background: var(--brand-red);
    color: #fff;
    font-weight: 900;
    font-size: 15px;
    letter-spacing: .5px;
    padding: 3px 8px;
    text-transform: uppercase;
  }
  .label--heading { display: block; width: max-content; margin: 0 auto 16px; }
  .field-row { display: flex; align-items: flex-end; gap: 8px; font-size: 13px; font-weight: 700; color: var(--muted); }
  .field-row .fill { flex: 1; border-bottom: 2px dotted var(--dots); height: 12px; }
  .ampm { display: flex; gap: 10px; align-items: center; }
  .ampm span { display: flex; align-items: center; gap: 3px; font-size: 11px; }
  .checkbox {
    display: inline-block;
    border: 2px solid var(--brand-red);
    border-radius: 3px;
    width: 16px; height: 16px;
    background: #fff;
  }
  .checkbox--small { width: 13px; height: 13px; }
  .days { display: flex; justify-content: space-between; margin: 18px 10px 16px; }
  .day { display: flex; align-items: center; gap: 5px; font-weight: 900; font-size: 15px; }
  .day .checkbox { width: 20px; height: 20px; }
  .therapist { margin-bottom: 16px; }
  .policy { text-align: center; }
  .policy .label { margin-bottom: 6px; font-size: 14px; }
  .policy p { font-size: 12px; font-weight: 700; color: var(--muted); line-height: 1.35; }

  /* Business side */
  .person { position: absolute; left: 28px; top: 80px; }
  .person__name { color: var(--brand-red); font-weight: 900; font-size: 22px; line-height: 1; }
  .person__title { font-weight: 700; font-size: 14px; letter-spacing: .3px; margin-top: 3px; }
  .brand {
    position: absolute; right: 24px; top: 30px;
    display: flex; align-items: center; gap: 10px;
  }
  .brand__mark { width: 48px; height: 48px; background: var(--brand-red); }
  .brand__name { color: var(--brand-red); font-weight: 700; font-size: 22px; }
  .tagline {
    position: absolute; right: 24px; top: 150px;
    text-align: right; color: var(--brand-red);
    font-weight: 700; font-size: 14px; line-height: 1.35;
  }
  .contact { position: absolute; left: 28px; bottom: 24px; font-size: 15px; font-weight: 700; }
  .contact li { list-style: none; display: flex; align-items: center; gap: 10px; margin-top: 8px; }
  .contact svg { width: 18px; height: 16px; fill: var(--brand-red); }
  .contact .web { font-weight: 900; font-size: 17px; }
  .contact .web em { font-style: normal; color: var(--brand-red); }
</style>
</head>
<body>

<section class="card card--appointment" aria-label="Appointment card">
  <span class="label label--heading">Next Appointment</span>
  <div class="field-row">
    <span>DATE:</span><span class="fill"></span>
    <span>TIME:</span><span class="fill"></span>
    <div class="ampm">
      <span>AM <i class="checkbox checkbox--small"></i></span>
      <span>PM <i class="checkbox checkbox--small"></i></span>
    </div>
  </div>
  <div class="days">
    <span class="day">Mon <i class="checkbox"></i></span>
    <span class="day">Tue <i class="checkbox"></i></span>
    <span class="day">Wed <i class="checkbox"></i></span>
    <span class="day">Thu <i class="checkbox"></i></span>
    <span class="day">Fri <i class="checkbox"></i></span>
  </div>
  <div class="field-row therapist">
    <span>NAME OF THERAPIST:</span><span class="fill"></span>
  </div>
  <div class="policy">
    <span class="label">Cancellation Policy</span>
    <p>Minimum of 24hrs notice is required prior to appointment time or full<br>treatment fees with apply</p>
  </div>
</section>

<section class="card card--business" aria-label="Business card">
  <div class="brand">
    <span class="brand__mark"></span>
    <span class="brand__name">Shoreline Myotherapy</span>
  </div>
  <div class="person">
    <div class="person__name">YOUR NAME</div>
    <div class="person__title">DESIGNATION</div>
  </div>
  <p class="tagline">Assists you to overcome<br>Acute &amp; Chronic pain &amp; injury<br>through Coastal Body Remedies</p>
  <ul class="contact">
    <li>
      <svg viewBox="0 0 18 16" aria-hidden="true"><path d="M2 4c0-2 3-3 7-3s7 1 7 3v2h-4V4.5H6V6H2zM5 7h8l2 7H3z"/><circle cx="9" cy="10.5" r="2" fill="#fff"/></svg>
      +61 400 555 018
    </li>
    <li>
      <svg viewBox="0 0 18 16" aria-hidden="true"><path d="M1 3h16v11H1z"/><path d="M1.5 3.5 9 9.5l7.5-6" fill="none" stroke="#fff" stroke-width="1.4"/></svg>
      Info@shorelinemyo.com.au
    </li>
    <li class="web">www.<em>shorelinemyo</em>.com.au</li>
  </ul>
</section>

</body>
</html>
```